Treatment Info-Graphic Poster

22 x 28 poster. We need a design for a poster to hang in our treatment rooms that quickly compares different treatments we offer and sets expectations for the patient. Attached is something I very quickly created on Excel, but we would like one that matches our company colors and looks much more polished. I have attached a info-graphic we have had designed prior for reference.

Target Market(s)

Osteoarthritis of the knee patients treatment comparison info graphic for poster

Font styles to use
Serif

Colors
85cae6
f78f20

Requirements
Must have
• Branded treatment comparison table
Nice to have
• Treatment graphics

```html
<!DOCTYPE html>
<html lang="en">
<head>
<meta charset="utf-8">
<title>Knee OA Treatment Comparison Poster</title>
<link href="https://fonts.googleapis.com/css2?family=Lato:wght@400;700&family=Source+Serif+4:wght@400;600&display=swap" rel="stylesheet">
<style>
:root{
  --sky:#85cae6;
  --orange:#f78f20;
  --teal-title:#2a7fa6;
  --brand-teal:#5aa9b6;
  --blue-mid:#29a3dc;
  --blue-deep:#1b7fc4;
  --blue-navy:#0d4c94;
  --blue-light:#6cc8f0;
  --label-grey:#8c8c8c;
  --cell-dark:#d6d6d6;
  --cell-light:#eeeeee;
  --ink:#3a3a3a;
  --page:#e6e6e6;
  --white:#ffffff;
}
*{box-sizing:border-box;margin:0;padding:0}
html,body{width:1200px;height:1200px;overflow:hidden;background:var(--page)}
.poster{position:absolute;left:152px;top:30px;width:896px;height:1140px;background:var(--white);overflow:hidden;font-family:"Lato",Arial,sans-serif}
.poster-art{position:absolute;left:0;top:0;width:896px;height:1140px}
.title{position:absolute;left:0;width:896px;top:430px;text-align:center;font-weight:700;font-size:46px;color:var(--teal-title);letter-spacing:-0.5px}
.title-rule{position:absolute;left:80px;width:736px;top:498px;height:2px;background:var(--orange)}
.compare{position:absolute;left:118px;top:518px;width:680px;display:grid;grid-template-columns:150px repeat(4,1fr);font-size:10px;color:var(--ink)}
.brand-cell{grid-row:1 / span 3;display:flex;flex-direction:column;align-items:center;justify-content:center;background:var(--white);border-top-left-radius:18px;gap:6px}
.brand-name{display:flex;align-items:center;gap:7px;font-family:"Source Serif 4",Georgia,serif;font-weight:600;font-size:23px;color:var(--brand-teal);white-space:nowrap}
.brand-mark{width:12px;height:12px;background:var(--brand-teal)}
.brand-tag{font-family:"Source Serif 4",Georgia,serif;font-size:13px;color:#6b6b6b}
.col-name{height:46px;display:flex;align-items:center;justify-content:center;gap:8px;text-align:center;font-size:15px;line-height:1.05;color:#0f3d66;background:var(--blue-mid);border-left:1px solid var(--white)}
.col-abbr{height:42px;display:flex;align-items:center;justify-content:center;gap:6px;font-family:"Source Serif 4",Georgia,serif;font-size:17px;color:var(--white);background:var(--blue-deep);border-left:1px solid var(--white);border-top:1px solid var(--white)}
.col-name.brace{background:var(--blue-light);border-top-right-radius:18px}
.col-abbr.brace{background:var(--blue-light)}
.col-name.stem{background:var(--blue-deep)}
.col-abbr.stem{background:#2896d8}
.options{background:#f4f4f4;border-left:1px solid var(--white);padding:3px 4px 4px}
.opt-row{display:grid;grid-template-columns:1fr 36px;column-gap:3px;height:18px;align-items:center;border-bottom:1px solid #d4d4d4;font-size:6.5px;line-height:1.1;color:#555}
.opt-row span:last-child{text-align:right;font-size:7.5px;white-space:nowrap}
.opt-row.head{height:12px;border-bottom:none}
.opt-row.head span:last-child{font-size:6px;color:#777}
.feature{height:27px;display:flex;align-items:center;justify-content:center;text-align:center;padding:0 6px;background:var(--label-grey);color:var(--white);font-size:11.5px;line-height:1.02;border-top:1px solid var(--white)}
.feature.last{border-bottom-left-radius:18px}
.cell{height:27px;display:flex;align-items:center;justify-content:center;border-left:1px solid var(--white);border-top:1px solid var(--white)}
.row-dark{background:var(--cell-dark)}
.row-light{background:var(--cell-light)}
.icon{width:12px;height:12px}
.last-cell{border-bottom-right-radius:18px}
</style>
</head>
<body>
<main class="poster">
  <svg class="poster-art" viewBox="0 0 896 1140">
    <defs>
      <linearGradient id="photoTone" x1="0" y1="0" x2="1" y2="1">
        <stop offset="0" stop-color="#eef1f2"/>
        <stop offset="0.45" stop-color="#c9cfd3"/>
        <stop offset="1" stop-color="#7f8a93"/>
      </linearGradient>
      <linearGradient id="bottomBlue" x1="0" y1="0" x2="1" y2="1">
        <stop offset="0" stop-color="#2a9ee0"/>
        <stop offset="1" stop-color="#0d4c94"/>
      </linearGradient>
    </defs>
    <path role="img" aria-label="Photo of a doctor reviewing a clipboard with a patient seated on an exam table"
      fill="url(#photoTone)"
      d="M0 0 H896 V270 C760 360 600 390 430 380 C260 370 110 330 0 280 Z"/>
    <path fill="none" stroke="var(--sky)" stroke-width="16" d="M0 292 C140 360 300 400 470 400 C640 400 780 370 896 300"/>
    <path fill="none" stroke="var(--orange)" stroke-width="6" d="M500 410 C660 404 790 370 896 330"/>
    <path fill="#e9f3fa" d="M0 860 C200 980 520 1000 896 930 V1140 H0 Z"/>
    <path fill="url(#bottomBlue)" d="M0 880 C140 1020 500 1060 896 1000 V1140 H0 Z"/>
    <path fill="none" stroke="#ffffff" stroke-width="5" d="M60 1020 C300 1080 600 1070 860 1030"/>
    <path fill="var(--blue-navy)" opacity="0.7" d="M300 1140 C520 1100 720 1070 896 1040 V1140 Z"/>
  </svg>

  <h1 class="title">Knee oA Treatment Comparison</h1>
  <div class="title-rule"></div>

  <section class="compare" aria-label="Treatment comparison table">
    <div class="brand-cell">
      <div class="brand-name"><span class="brand-mark"></span>Stridewell</div>
      <div class="brand-tag">Knee Specialists</div>
    </div>

    <div class="col-name">Hyaluronic<br>Acid
      <svg class="icon" viewBox="0 0 14 14"><path d="M2 12 L10 4 M8 2 L12 6 M10 4 L13 1" stroke="#fff" stroke-width="2" fill="none"/></svg></div>
    <div class="col-name">Platelet<br>Rich
      <svg class="icon" viewBox="0 0 14 14"><path d="M2 12 L10 4 M8 2 L12 6 M10 4 L13 1" stroke="#fff" stroke-width="2" fill="none"/></svg></div>
    <div class="col-name stem">Stem Cell<br>Therapy</div>
    <div class="col-name brace">Knee Brace</div>

    <div class="col-abbr">(HA)</div>
    <div class="col-abbr">Plasma (PRP)</div>
    <div class="col-abbr stem">&amp; PRP
      <svg class="icon" viewBox="0 0 14 14"><path d="M2 12 L10 4 M8 2 L12 6 M10 4 L13 1" stroke="#fff" stroke-width="2" fill="none"/></svg></div>
    <div class="col-abbr brace"></div>

    <div class="options">
      <div class="opt-row head"><span></span><span>OA Grade</span></div>
      <div class="opt-row"><span>Single Injection (Lubra One)</span><span>1,2,3,4</span></div>
      <div class="opt-row"><span>Single Injection (Duraglide)</span><span>1,2,3,4</span></div>
      <div class="opt-row"><span>3 Part Injection Series (Synogel)</span><span>1,2,3,4</span></div>
      <div class="opt-row"><span>3/4 Part Injection Series (Viscorth)</span><span>1,2,3,4</span></div>
    </div>
    <div class="options">
      <div class="opt-row head"><span></span><span>OA Grade</span></div>
      <div class="opt-row"><span>Single Injection (Plasmacel)</span><span>1,2</span></div>
      <div class="opt-row"><span>2 Part Injection Series</span><span>3,4</span></div>
      <div class="opt-row"><span></span><span></span></div>
      <div class="opt-row"><span></span><span></span></div>
    </div>
    <div class="options">
      <div class="opt-row head"><span></span><span>OA Grade</span></div>
      <div class="opt-row"><span>Single Injection</span><span>1,2,3,4</span></div>
      <div class="opt-row"><span></span><span></span></div>
      <div class="opt-row"><span></span><span></span></div>
      <div class="opt-row"><span></span><span></span></div>
    </div>
    <div class="options">
      <div class="opt-row head"><span></span><span>OA Grade</span></div>
      <div class="opt-row"><span>Kinetra 2</span><span>1,2,3,4</span></div>
      <div class="opt-row"><span>Patellar Stabilization</span><span>1,2,3,4</span></div>
      <div class="opt-row"><span></span><span></span></div>
      <div class="opt-row"><span></span><span></span></div>
    </div>

    <div class="feature">Cushion &amp; Lubricate</div>
    <div class="cell row-light"><svg class="icon" viewBox="0 0 14 14"><circle cx="7" cy="7" r="6" fill="none" stroke="#888"/><path d="M4 7 L6.3 9.3 L10.5 4.5" fill="none" stroke="#888" stroke-width="1.3"/></svg></div>
    <div class="cell row-light"><svg class="icon" viewBox="0 0 14 14"><circle cx="7" cy="7" r="6" fill="none" stroke="#888"/><path d="M4 7 L6.3 9.3 L10.5 4.5" fill="none" stroke="#888" stroke-width="1.3"/></svg></div>
    <div class="cell row-light"><svg class="icon" viewBox="0 0 14 14"><circle cx="7" cy="7" r="6" fill="none" stroke="#888"/><path d="M4 7 L6.3 9.3 L10.5 4.5" fill="none" stroke="#888" stroke-width="1.3"/></svg></div>
    <div class="cell row-light"></div>

    <div class="feature">Decrease Inflammation</div>
    <div class="cell row-dark"><svg class="icon" viewBox="0 0 14 14"><circle cx="7" cy="7" r="6" fill="none" stroke="#888"/><path d="M4 7 L6.3 9.3 L10.5 4.5" fill="none" stroke="#888" stroke-width="1.3"/></svg></div>
    <div class="cell row-dark"><svg class="icon" viewBox="0 0 14 14"><circle cx="7" cy="7" r="6" fill="none" stroke="#888"/><path d="M4 7 L6.3 9.3 L10.5 4.5" fill="none" stroke="#888" stroke-width="1.3"/></svg></div>
    <div class="cell row-dark"><svg class="icon" viewBox="0 0 14 14"><circle cx="7" cy="7" r="6" fill="none" stroke="#888"/><path d="M4 7 L6.3 9.3 L10.5 4.5" fill="none" stroke="#888" stroke-width="1.3"/></svg></div>
    <div class="cell row-dark"></div>

    <div class="feature">Stimulates Synovial Production of HA</div>
    <div class="cell row-light"><svg class="icon" viewBox="0 0 14 14"><circle cx="7" cy="7" r="6" fill="none" stroke="#888"/><path d="M4 7 L6.3 9.3 L10.5 4.5" fill="none" stroke="#888" stroke-width="1.3"/></svg></div>
    <div class="cell row-light"><svg class="icon" viewBox="0 0 14 14"><circle cx="7" cy="7" r="6" fill="none" stroke="#888"/><path d="M4 7 L6.3 9.3 L10.5 4.5" fill="none" stroke="#888" stroke-width="1.3"/></svg></div>
    <div class="cell row-light"><svg class="icon" viewBox="0 0 14 14"><circle cx="7" cy="7" r="6" fill="none" stroke="#888"/><path d="M4 7 L6.3 9.3 L10.5 4.5" fill="none" stroke="#888" stroke-width="1.3"/></svg></div>
    <div class="cell row-light"></div>

    <div class="feature">Healing Properties</div>
    <div class="cell row-dark"></div>
    <div class="cell row-dark"><svg class="icon" viewBox="0 0 14 14"><circle cx="7" cy="7" r="6" fill="none" stroke="#888"/><path d="M4 7 L6.3 9.3 L10.5 4.5" fill="none" stroke="#888" stroke-width="1.3"/></svg></div>
    <div class="cell row-dark"><svg class="icon" viewBox="0 0 14 14"><circle cx="7" cy="7" r="6" fill="none" stroke="#888"/><path d="M4 7 L6.3 9.3 L10.5 4.5" fill="none" stroke="#888" stroke-width="1.3"/></svg></div>
    <div class="cell row-dark"></div>

    <div class="feature">Repairative Properties</div>
    <div class="cell row-light"></div>
    <div class="cell row-light"></div>
    <div class="cell row-light"><svg class="icon" viewBox="0 0 14 14"><circle cx="7" cy="7" r="6" fill="none" stroke="#888"/><path d="M4 7 L6.3 9.3 L10.5 4.5" fill="none" stroke="#888" stroke-width="1.3"/></svg></div>
    <div class="cell row-light"></div>

    <div class="feature">Potential Cartilage Regeneration</div>
    <div class="cell row-dark"></div>
    <div class="cell row-dark"></div>
    <div class="cell row-dark"><svg class="icon" viewBox="0 0 14 14"><circle cx="7" cy="7" r="6" fill="none" stroke="#888"/><path d="M4 7 L6.3 9.3 L10.5 4.5" fill="none" stroke="#888" stroke-width="1.3"/></svg></div>
    <div class="cell row-dark"><svg class="icon" viewBox="0 0 14 14"><circle cx="7" cy="7" r="6" fill="none" stroke="#888"/><path d="M4 7 L6.3 9.3 L10.5 4.5" fill="none" stroke="#888" stroke-width="1.3"/></svg></div>

    <div class="feature">On Average, Benefits Last 4-6 Months</div>
    <div class="cell row-light"><svg class="icon" viewBox="0 0 14 14"><circle cx="7" cy="7" r="6" fill="none" stroke="#888"/><path d="M4 7 L6.3 9.3 L10.5 4.5" fill="none" stroke="#888" stroke-width="1.3"/></svg></div>
    <div class="cell row-light"><svg class="icon" viewBox="0 0 14 14"><circle cx="7" cy="7" r="6" fill="none" stroke="#888"/><path d="M4 7 L6.3 9.3 L10.5 4.5" fill="none" stroke="#888" stroke-width="1.3"/></svg></div>
    <div class="cell row-light"><svg class="icon" viewBox="0 0 14 14"><circle cx="7" cy="7" r="6" fill="none" stroke="#888"/><path d="M4 7 L6.3 9.3 L10.5 4.5" fill="none" stroke="#888" stroke-width="1.3"/></svg></div>
    <div class="cell row-light"><svg class="icon" viewBox="0 0 14 14"><circle cx="7" cy="7" r="6" fill="none" stroke="#888"/><path d="M4 7 L6.3 9.3 L10.5 4.5" fill="none" stroke="#888" stroke-width="1.3"/></svg></div>

    <div class="feature">On Average, Benefits Last 6-12 Months</div>
    <div class="cell row-dark"></div>
    <div class="cell row-dark"><svg class="icon" viewBox="0 0 14 14"><circle cx="7" cy="7" r="6" fill="none" stroke="#888"/><path d="M4 7 L6.3 9.3 L10.5 4.5" fill="none" stroke="#888" stroke-width="1.3"/></svg></div>
    <div class="cell row-dark"><svg class="icon" viewBox="0 0 14 14"><circle cx="7" cy="7" r="6" fill="none" stroke="#888"/><path d="M4 7 L6.3 9.3 L10.5 4.5" fill="none" stroke="#888" stroke-width="1.3"/></svg></div>
    <div class="cell row-dark"><svg class="icon" viewBox="0 0 14 14"><circle cx="7" cy="7" r="6" fill="none" stroke="#888"/><path d="M4 7 L6.3 9.3 L10.5 4.5" fill="none" stroke="#888" stroke-width="1.3"/></svg></div>

    <div class="feature">On Average, Benefits Last 18+ Months</div>
    <div class="cell row-light"></div>
    <div class="cell row-light"></div>
    <div class="cell row-light"><svg class="icon" viewBox="0 0 14 14"><circle cx="7" cy="7" r="6" fill="none" stroke="#888"/><path d="M4 7 L6.3 9.3 L10.5 4.5" fill="none" stroke="#888" stroke-width="1.3"/></svg></div>
    <div class="cell row-light"><svg class="icon" viewBox="0 0 14 14"><circle cx="7" cy="7" r="6" fill="none" stroke="#888"/><path d="M4 7 L6.3 9.3 L10.5 4.5" fill="none" stroke="#888" stroke-width="1.3"/></svg></div>

    <div class="feature">Corrects Biomechanics &amp; Stabilizes Joint</div>
    <div class="cell row-dark"></div>
    <div class="cell row-dark"></div>
    <div class="cell row-dark"></div>
    <div class="cell row-dark"><svg class="icon" viewBox="0 0 14 14"><circle cx="7" cy="7" r="6" fill="none" stroke="#888"/><path d="M4 7 L6.3 9.3 L10.5 4.5" fill="none" stroke="#888" stroke-width="1.3"/></svg></div>

    <div class="feature last">Covered by MOST Insurance</div>
    <div class="cell row-light"><svg class="icon" viewBox="0 0 14 14"><circle cx="7" cy="7" r="6" fill="none" stroke="#888"/><path d="M4 7 L6.3 9.3 L10.5 4.5" fill="none" stroke="#888" stroke-width="1.3"/></svg></div>
    <div class="cell row-light"></div>
    <div class="cell row-light"></div>
    <div class="cell row-light last-cell"></div>
  </section>
</main>
</body>
</html>
```